依頼概要
■ 依頼の目的/概要

育毛剤・シャンプーのランキングサイトのデザインをお願い致します。

■ デザインへの要望

・イメージ画像として人間(できれば女性)の写真もしくは、イラストを使用してください。
・ランキングの順位と商品の特徴(写真や文字)をメインに強調したデザインにしてください。
・サイトを訪れた際に育毛剤・シャンプーのランキングサイトであることがわかるようにしてください。
・ランキングの上位3件ほどがはっきりと見えるようにしてください。
・ランキングサイトの参考として以下に、いくつか参考URLを記載しておきます。
・http://xn--7pqt52fkwa.net/
・http://xn--7pqt52fzmc.com/
・http://www.tyvalpeq.org/
・http://www.sorafumikiri-junban.com/
・http://tanepoka.v-nest.net/

■ 納品ファイルの希望

フォトショップ形式(.psd形式)でお願い致します。

■ 利用用途

主に育毛剤・シャンプーのランキングサイトに使用させて頂きます。

■ 進め方

弊社の希望するイメージに近い提案を1つ(場合によって複数)選択させて頂きます。希望に近づけるために、修正要望を個別にさせて頂くこともあります。コンペ方式のため、修正後に当選されない場合も、どうかご了承ください。

■ その他/注意点

選択させて頂いたデザインの著作権(財産権)等の扱いはBravoly利用規約に従い、弊社に譲渡をお願いします。フォントや画像素材などを利用する場合は上記利用用途に使用できることを確認し、第三者の知的財産権等に注意して下さい。
補足:
今回はサイトのトップページのデザインのみでも結構です。

トップページに必要な内容ですが、
サイトを訪れた際に育毛剤ランキングへのリンクと、シャンプーランキングへのリンクとランキングの上位3位までは、表示できるようにして下さい。
(最初に表示されるのは育毛剤ランキングでお願い致します)

トップページの項目としては以下のようにお願い致します。
ナビゲーション(育毛剤ランキングへのリンクとシャンプーランキングへのリンク), 商品名, 商品の特徴を表した一文(※), 価格, 容量, 男女兼用かどうか, 評判(☆を使うなどわかりやすく), 販売サイトへのリンク

サイトのロゴや基調となる色の指定は、暖色系を基調としてください。

※商品の特徴を表した一文の例文と致しましては、「発毛率No.1の育毛サプリメント!」や「発毛率96%、平均1~2ヶ月の発毛スピード!」また、「30日で満足できないなら全額返金!」などです。
■ 選んだ理由

今回minteluさんの提案を当選とさせて頂いた理由と致しましては、
要望に対してイメージ通りの提案をして下さったことです。

修正依頼に対しても誠意をもって応じて下さったので、
この提案を当選とさせて頂きました。

■ 提案者全員へのお礼・コメント

皆様、ご提案ありがとうございました。
弊社としましても非常に選考に苦労いたしました。

落選された方には残念な結果にはなったのですが、
今後とも機会がございましたら、よろしくお願い致します。

```html
<!DOCTYPE html>
<html lang="ja">
<head>
<meta charset="utf-8">
<title>育毛剤・シャンプーのランキングサイト</title>
<link href="https://fonts.googleapis.com/css2?family=M+PLUS+Rounded+1c:wght@500;800&family=Noto+Sans+JP:wght@400;700&display=swap" rel="stylesheet">
<style>
:root{
  --orange:#f39200;
  --orange-dark:#e07400;
  --cream:#fff7ea;
  --text:#333;
  --muted:#777;
  --gold:#e8b400;
  --silver:#a8a8a8;
  --bronze:#c07a3a;
  --star:#f5b800;
}
*{margin:0;padding:0;box-sizing:border-box}
html,body{width:887px;height:1200px;overflow:hidden}
body{font-family:"Noto Sans JP",sans-serif;color:var(--text);background:#fff;position:relative}
.ticker{position:absolute;top:0;left:0;width:100%;height:24px;background:var(--orange);color:#fff;font-size:11px;line-height:24px;padding-left:14px;white-space:nowrap;overflow:hidden;z-index:2}
.nav{position:absolute;top:32px;left:14px;display:flex;gap:6px;z-index:2}
.nav a{display:block;background:linear-gradient(#ffa629,var(--orange-dark));color:#fff;font-size:12px;font-weight:700;padding:3px 14px;border-radius:3px;text-decoration:none}
.header{position:absolute;top:24px;left:0;width:100%;height:196px;background:linear-gradient(#fff,var(--cream))}
.hero{position:absolute;right:0;top:0;width:300px;height:196px;background:linear-gradient(120deg,#f6e9d8,#8a5a3a 55%,#3a2518)}
.brand{position:absolute;left:40px;top:66px}
.updated{font-size:11px;color:var(--muted);margin-left:50px}
.site-title{display:flex;align-items:center;gap:10px;font-family:"M PLUS Rounded 1c",sans-serif;font-weight:800;font-size:26px;color:var(--orange)}
.site-title .mark{width:40px;height:40px;border-radius:50%;background:var(--orange)}
.ranking{position:absolute;left:0;width:100%}
.r1{top:236px}
.r2{top:630px}
.section-head{margin:0 auto;width:770px;height:36px;background:linear-gradient(#ffb447,var(--orange));border-radius:18px;color:#fff;text-align:center;font-family:"M PLUS Rounded 1c",sans-serif;font-weight:800;font-size:19px;line-height:36px}
.cards{width:760px;margin:10px auto 0;display:flex;justify-content:space-between}
.card{width:232px;height:300px;border:2px solid var(--orange);border-radius:6px;background:#fff;text-align:center;overflow:hidden}
.rank{display:flex;align-items:center;justify-content:center;gap:6px;height:26px;background:linear-gradient(#ffb447,var(--orange));color:#fff;font-weight:700;font-size:14px}
.rank svg{width:18px;height:14px}
.product-name{margin:8px 10px 0;padding:4px;background:var(--cream);color:var(--orange-dark);font-weight:700;font-size:11px;line-height:1.4;height:40px;display:flex;align-items:center;justify-content:center}
.catch{font-size:10px;margin:8px 6px;height:14px;line-height:14px;white-space:nowrap}
.product-img{width:34px;height:92px;margin:4px auto 10px;border-radius:4px;background:linear-gradient(90deg,#0c3a2a,#2f7a55 50%,#0c3a2a)}
.spec{width:190px;margin:0 auto;border-collapse:collapse;font-size:10px;text-align:left}
.spec th,.spec td{border-bottom:1px dotted #ccc;padding:0 2px;height:20px;font-weight:400}
.spec th{color:var(--muted);width:70px}
.stars{color:var(--star)}
.more{width:760px;margin:6px auto 0;text-align:right;font-size:11px;color:var(--orange-dark);font-weight:700}
.more::before{content:"▶ ";font-size:9px}
.footer-links{position:absolute;top:1018px;width:100%;text-align:center;font-size:11px;color:var(--orange-dark)}
.copyright{position:absolute;top:1044px;width:100%;height:22px;background:var(--orange);color:#fff;font-size:10px;line-height:22px;text-align:center}
</style>
</head>
<body>
<div class="ticker">育毛剤・シャンプーの人気ランキングサイト。あなたに合う育毛剤とシャンプーを比較して見つけよう。</div>
<nav class="nav"><a href="#">ホーム</a><a href="#">育毛剤ランキング</a><a href="#">シャンプーランキング</a></nav>
<header class="header">
  <div class="hero" role="img" aria-label="長い髪をなびかせる女性の写真"></div>
  <div class="brand">
    <p class="updated">ランキング更新日：2015/05/15</p>
    <h1 class="site-title"><span class="mark"></span>育毛剤・シャンプーのランキングサイト</h1>
  </div>
</header>

<section class="ranking r1">
  <h2 class="section-head">育毛剤ランキング</h2>
  <div class="cards">
    <article class="card">
      <div class="rank"><svg viewBox="0 0 20 16"><path d="M1 4l5 5 4-8 4 8 5-5-2 11H3z" fill="var(--gold)"/></svg>1位</div>
      <p class="product-name">〜 サンプル育毛剤A 〜</p>
      <p class="catch">発毛率No.1の育毛サプリメント!</p>
      <div class="product-img" role="img" aria-label="育毛剤ボトルの商品写真"></div>
      <table class="spec"><tr><th>価格</th><td>9,800円</td></tr><tr><th>容量</th><td>200 ml</td></tr><tr><th>男女兼用</th><td>○</td></tr><tr><th>評判</th><td class="stars">★★★★★</td></tr></table>
    </article>
    <article class="card">
      <div class="rank"><svg viewBox="0 0 20 16"><path d="M1 4l5 5 4-8 4 8 5-5-2 11H3z" fill="var(--silver)"/></svg>2位</div>
      <p class="product-name">〜 サンプル育毛剤B 〜<br>30日で満足できないなら全額返金</p>
      <p class="catch">発毛率96%、平均1〜2ヶ月の発毛スピード!</p>
      <div class="product-img" role="img" aria-label="育毛剤ボトルの商品写真"></div>
      <table class="spec"><tr><th>価格</th><td>9,800円</td></tr><tr><th>容量</th><td>200 ml</td></tr><tr><th>男女兼用</th><td>○</td></tr><tr><th>評判</th><td class="stars">★★★★☆</td></tr></table>
    </article>
    <article class="card">
      <div class="rank"><svg viewBox="0 0 20 16"><path d="M1 4l5 5 4-8 4 8 5-5-2 11H3z" fill="var(--bronze)"/></svg>3位</div>
      <p class="product-name">〜 サンプル育毛剤C 〜</p>
      <p class="catch">発毛率No.1の育毛サプリメント!</p>
      <div class="product-img" role="img" aria-label="育毛剤ボトルの商品写真"></div>
      <table class="spec"><tr><th>価格</th><td>9,800円</td></tr><tr><th>容量</th><td>200 ml</td></tr><tr><th>男女兼用</th><td>○</td></tr><tr><th>評判</th><td class="stars">★★★☆☆</td></tr></table>
    </article>
  </div>
  <p class="more">育毛剤ランキング</p>
</section>

<section class="ranking r2">
  <h2 class="section-head">シャンプーランキング</h2>
  <div class="cards">
    <article class="card">
      <div class="rank"><svg viewBox="0 0 20 16"><path d="M1 4l5 5 4-8 4 8 5-5-2 11H3z" fill="var(--gold)"/></svg>1位</div>
      <p class="product-name">〜 サンプルシャンプーA 〜</p>
      <p class="catch">発毛率No.1の育毛サプリメント!</p>
      <div class="product-img" role="img" aria-label="シャンプーボトルの商品写真"></div>
      <table class="spec"><tr><th>価格</th><td>9,800円</td></tr><tr><th>容量</th><td>200 ml</td></tr><tr><th>男女兼用</th><td>○</td></tr><tr><th>評判</th><td class="stars">★★★★★</td></tr></table>
    </article>
    <article class="card">
      <div class="rank"><svg viewBox="0 0 20 16"><path d="M1 4l5 5 4-8 4 8 5-5-2 11H3z" fill="var(--silver)"/></svg>2位</div>
      <p class="product-name">〜 サンプルシャンプーB 〜<br>30日で満足できないなら全額返金</p>
      <p class="catch">発毛率96%、平均1〜2ヶ月の発毛スピード!</p>
      <div class="product-img" role="img" aria-label="シャンプーボトルの商品写真"></div>
      <table class="spec"><tr><th>価格</th><td>9,800円</td></tr><tr><th>容量</th><td>200 ml</td></tr><tr><th>男女兼用</th><td>○</td></tr><tr><th>評判</th><td class="stars">★★★★☆</td></tr></table>
    </article>
    <article class="card">
      <div class="rank"><svg viewBox="0 0 20 16"><path d="M1 4l5 5 4-8 4 8 5-5-2 11H3z" fill="var(--bronze)"/></svg>3位</div>
      <p class="product-name">〜 サンプルシャンプーC 〜</p>
      <p class="catch">発毛率No.1の育毛サプリメント!</p>
      <div class="product-img" role="img" aria-label="シャンプーボトルの商品写真"></div>
      <table class="spec"><tr><th>価格</th><td>9,800円</td></tr><tr><th>容量</th><td>200 ml</td></tr><tr><th>男女兼用</th><td>○</td></tr><tr><th>評判</th><td class="stars">★★★☆☆</td></tr></table>
    </article>
  </div>
  <p class="more">シャンプーランキング</p>
</section>

<p class="footer-links">サイトマップ ｜ お問い合わせ</p>
<footer class="copyright">Copyright (C) 2015 育毛剤・シャンプーのランキングサイト All Rights Reserved.</footer>
</body>
</html>
```